VEMRI Business Card

We want a fresh and clean look with a modern touch for our new business cards.
Please use our Logo and incorporate very similar colours blues/grey/white.
Logo used on back and front.
Info on back: name, email address, phone number, website, address (Eastbrook, NSW) - please use samples for other info.
Here is website https://www.vemri-example.de/en/
Contact Information for Business Card
Please use our Logo and incorporate very similar colours blues/grey/white. Logo used on back and front. Info on back: name, email address, phone number, website, address (Eastbrook, NSW) - please use samples for other info. Here is website https://www.vemri-example.de/en/
- Matching Logo or website/catalogue

```html
<!DOCTYPE html>
<html lang="en">
<head>
<meta charset="utf-8">
<title>VEMRI Business Card</title>
<link rel="stylesheet" href="https://fonts.googleapis.com/css2?family=Montserrat:wght@400;500;700;800&display=swap">
<style>
  :root {
    --stage: #2b2d30;
    --navy: #021d45;
    --brand-blue: #1a4fa3;
    --ink: #111418;
    --steel-light: #eef0f3;
    --steel: #9aa3ae;
    --lube-blue: #3c63b5;
    --paper: #ffffff;
  }
  * { box-sizing: border-box; margin: 0; padding: 0; }
  html, body { width: 1200px; height: 939px; overflow: hidden; }
  body {
    background: var(--stage);
    font-family: "Montserrat", Arial, sans-serif;
    position: relative;
  }
  .card {
    position: absolute;
    width: 640px;
    height: 366px;
    box-shadow: 0 14px 30px rgba(0,0,0,.45);
    overflow: hidden;
  }
  .card--front { left: 120px; top: 70px; background: var(--navy); }
  .card--back {
    left: 440px; top: 490px; background: var(--paper);
    border-bottom: 4px solid var(--brand-blue);
    border-left: 2px solid var(--brand-blue);
  }
  .wordmark {
    display: flex; align-items: center; gap: 14px;
    font-weight: 700; letter-spacing: 2px; line-height: 1;
  }
  .wordmark__dot { border-radius: 50%; background: var(--brand-blue); flex: none; }
  .card--front .wordmark {
    position: absolute; left: 50%; top: 50%;
    transform: translate(-50%, -50%);
    color: var(--paper); font-size: 86px;
  }
  .card--front .wordmark__dot { width: 46px; height: 46px; }
  .card--back .wordmark {
    position: absolute; left: 40px; top: 74px;
    color: var(--ink); font-size: 52px;
  }
  .card--back .wordmark__dot { width: 28px; height: 28px; }
  .person { position: absolute; left: 48px; top: 168px; }
  .person__name {
    color: var(--brand-blue); font-weight: 800; font-size: 27px; letter-spacing: .5px;
  }
  .person__role { color: var(--ink); font-size: 15px; font-weight: 500; margin-top: 4px; margin-left: 14px; }
  .contact { list-style: none; position: absolute; left: 62px; top: 246px; }
  .contact li {
    display: flex; align-items: center; gap: 9px;
    font-size: 14px; color: var(--ink); height: 23px; white-space: nowrap;
  }
  .contact svg { width: 13px; height: 13px; fill: var(--brand-blue); flex: none; }
  .visual {
    position: absolute; right: 0; top: 0; width: 290px; height: 270px;
    background: radial-gradient(ellipse at 62% 42%, var(--steel-light) 0%, var(--steel) 36%, var(--lube-blue) 60%, rgba(255,255,255,0) 74%);
  }
</style>
</head>
<body>
  <section class="card card--front">
    <div class="wordmark"><span class="wordmark__dot"></span>VEMRI</div>
  </section>

  <section class="card card--back">
    <div class="visual" role="img" aria-label="Steel roller bearing wrapped in swirling blue lubricant"></div>
    <div class="wordmark"><span class="wordmark__dot"></span>VEMRI</div>
    <div class="person">
      <p class="person__name">JHON DOE</p>
      <p class="person__role">Director</p>
    </div>
    <ul class="contact">
      <li><svg viewBox="0 0 24 24"><path d="M6.6 10.8a15.1 15.1 0 0 0 6.6 6.6l2.2-2.2c.3-.3.7-.4 1-.2 1.1.4 2.3.6 3.6.6.6 0 1 .4 1 1V20c0 .6-.4 1-1 1A17 17 0 0 1 3 4c0-.6.4-1 1-1h3.5c.6 0 1 .4 1 1 0 1.3.2 2.5.6 3.6.1.3 0 .7-.2 1z"/></svg>+49 (0) 12 34 / 5 67-0</li>
      <li><svg viewBox="0 0 24 24"><path d="M2 5h20v14H2z M3 6l9 7 9-7"/></svg>lubricants@vemri-example.de</li>
      <li><svg viewBox="0 0 24 24"><path d="M12 2a10 10 0 1 0 0 20 10 10 0 0 0 0-20zm6.9 6h-3a15 15 0 0 0-1.3-4A8 8 0 0 1 18.9 8zM12 4a13 13 0 0 1 1.9 4h-3.8A13 13 0 0 1 12 4zM4.3 14a8 8 0 0 1 0-4h3.4a16 16 0 0 0 0 4zm.8 2h3a15 15 0 0 0 1.3 4A8 8 0 0 1 5.1 16zm3-8h-3a8 8 0 0 1 4.3-4 15 15 0 0 0-1.3 4zM12 20a13 13 0 0 1-1.9-4h3.8A13 13 0 0 1 12 20zm2.3-6H9.7a14 14 0 0 1 0-4h4.6a14 14 0 0 1 0 4zm.3 6a15 15 0 0 0 1.3-4h3a8 8 0 0 1-4.3 4zm1.7-6a16 16 0 0 0 0-4h3.4a8 8 0 0 1 0 4z"/></svg>www.vemri-example.de</li>
      <li><svg viewBox="0 0 24 24"><path d="M12 2a7 7 0 0 0-7 7c0 5.3 7 13 7 13s7-7.7 7-13a7 7 0 0 0-7-7zm0 9.5a2.5 2.5 0 1 1 0-5 2.5 2.5 0 0 1 0 5z"/></svg>Eastbrook, NSW</li>
    </ul>
  </section>
</body>
</html>
```